High End Business Card Design for Flooring Store

Looking for a new card design for our hardwood flooring company. We have no print budget for these and are open to cards made from wood, metal, cardstock with embossed print ... or any combination of these. No plastic.

We sell luxury products and I want the cards to reflect our image of quality and class.

Our contact information as such;
Employee Name
418 Colbrook Blvd.
Dieppe, NB
K9R-3M5
(555) 214-3968
Employee email @velkaflooring.com

Target Market(s)

Home Builders

Contact Information for Business Card

Emnployee name, business contact information

```html
<!DOCTYPE html>
<html lang="en">
<head>
<meta charset="utf-8">
<title>Velka Flooring – Business Cards</title>
<link rel="stylesheet" href="https://fonts.googleapis.com/css2?family=Lato:wght@300;400;700&display=swap">
<style>
  :root {
    --backdrop: #2b2c2e;
    --card: #1f1f20;
    --red: #952b24;
    --red-deep: #7f241e;
    --yellow: #eab72a;
    --yellow-deep: #d9a620;
    --white: #f2f2f2;
  }
  * { box-sizing: border-box; margin: 0; padding: 0; }
  html, body { width: 1200px; height: 952px; overflow: hidden; }
  body {
    background: var(--backdrop);
    font-family: "Lato", sans-serif;
    position: relative;
  }
  .card {
    position: absolute;
    left: 280px;
    width: 640px;
    height: 366px;
    background: var(--card);
    overflow: hidden;
    box-shadow: 0 14px 30px rgba(0,0,0,.45);
  }
  .card-back { top: 70px; }
  .card-front { top: 506px; }

  .accent-red {
    position: absolute;
    left: 0; top: 0;
    width: 280px; height: 230px;
    background: linear-gradient(135deg, var(--red), var(--red-deep));
  }
  .accent-yellow {
    position: absolute;
    right: 0; bottom: 0;
    width: 250px; height: 286px;
    background: linear-gradient(180deg, var(--yellow), var(--yellow-deep));
  }

  .brand {
    position: absolute;
    display: flex;
    align-items: center;
    gap: 12px;
  }
  .brand-mark { background: var(--yellow); }
  .brand-name {
    color: var(--red);
    font-weight: 400;
    letter-spacing: 1px;
    line-height: 1;
  }
  .tagline {
    position: absolute;
    color: var(--white);
    font-weight: 400;
    line-height: 1.15;
  }
  .card-back .brand { left: 310px; top: 118px; }
  .card-back .brand-mark { width: 26px; height: 26px; }
  .card-back .brand-name { font-size: 80px; }
  .card-back .tagline { left: 348px; top: 214px; font-size: 20px; }
  .address {
    position: absolute;
    left: 110px; bottom: 40px;
    color: var(--yellow);
    font-size: 17px;
    font-weight: 400;
  }

  .card-front .brand { left: 52px; top: 40px; gap: 8px; }
  .card-front .brand-mark { width: 14px; height: 14px; }
  .card-front .brand-name { font-size: 38px; }
  .card-front .tagline { left: 74px; top: 86px; font-size: 10px; }
  .person { position: absolute; left: 52px; top: 132px; }
  .person-name { font-size: 38px; color: var(--white); font-weight: 300; letter-spacing: 1px; line-height: 1.1; }
  .person-name .first { color: var(--yellow); font-weight: 700; }
  .person-title { font-size: 15px; color: var(--white); margin-top: 6px; }
  .divider { width: 230px; height: 1px; background: var(--red); margin-top: 14px; }
  .contacts { position: absolute; left: 52px; top: 236px; list-style: none; }
  .contacts li {
    display: flex; align-items: center; gap: 10px;
    color: var(--white); font-size: 15px; margin-bottom: 9px;
  }
  .contacts svg { flex: none; }
</style>
</head>
<body>
  <section class="card card-back">
    <div class="accent-red" role="img" aria-label="Red decorative accent block"></div>
    <div class="brand">
      <span class="brand-mark"></span>
      <span class="brand-name">Velka</span>
    </div>
    <p class="tagline">Planchers &amp; Escaliers<br>Flooring &amp; Stairs</p>
    <p class="address">418 Colbrook Blvd. Dieppe, NB K9R-3M5</p>
  </section>

  <section class="card card-front">
    <div class="brand">
      <span class="brand-mark"></span>
      <span class="brand-name">Velka</span>
    </div>
    <p class="tagline">Planchers &amp; Escaliers<br>Flooring &amp; Stairs</p>
    <div class="person">
      <p class="person-name"><span class="first">MARTIN</span> HALE</p>
      <p class="person-title">Owner/ CEO</p>
      <div class="divider"></div>
    </div>
    <ul class="contacts">
      <li>
        <svg width="18" height="18" viewBox="0 0 18 18"><rect width="18" height="18" rx="2" fill="var(--red)"/><path d="M6 4.5c-1 .6-1.4 1.6-1 3 .8 2.6 2.9 4.8 5.5 5.6 1.3.4 2.3 0 3-1l-1.7-1.6-1.3.8c-1.3-.6-2.2-1.5-2.8-2.8l.8-1.3z" fill="var(--white)"/></svg>
        (555) 214-3968
      </li>
      <li>
        <svg width="18" height="18" viewBox="0 0 18 18"><rect width="18" height="18" rx="2" fill="var(--red)"/><rect x="4" y="5.5" width="10" height="7" fill="none" stroke="var(--white)" stroke-width="1.3"/><path d="M4 5.5l5 4 5-4" fill="none" stroke="var(--white)" stroke-width="1.3"/></svg>
        info@velkaflooring.com
      </li>
      <li>
        <svg width="18" height="18" viewBox="0 0 18 18"><rect width="18" height="18" rx="2" fill="var(--red)"/><circle cx="9" cy="9" r="5" fill="none" stroke="var(--white)" stroke-width="1.3"/><path d="M4 9h10M9 4c-2 2.8-2 7.2 0 10M9 4c2 2.8 2 7.2 0 10" fill="none" stroke="var(--white)" stroke-width="1.1"/></svg>
        www.velkaflooring.com
      </li>
    </ul>
    <div class="accent-yellow" role="img" aria-label="Yellow decorative accent block"></div>
  </section>
</body>
</html>
```